Keep Harbor Homestead. Avoid short sale, foreclosure, repossession, negative credit inquires and all other negative actions associated with your real estate.

Call 833-47-RENEW or info@keepharborhomestead.com

```html
<!DOCTYPE html>
<html lang="en">
<head>
<meta charset="utf-8">
<title>Keep Harbor Homestead</title>
<link rel="stylesheet" href="https://fonts.googleapis.com/css2?family=Bebas+Neue&family=Arimo:wght@400;700&display=swap">
<style>
  :root {
    --backdrop: #8a8a8a;
    --paper: #ffffff;
    --brand-blue: #0b8bd3;
    --body-grey: #7a7a7a;
    --on-blue: #ffffff;
  }
  * { margin: 0; padding: 0; box-sizing: border-box; }
  html, body {
    width: 891px;
    height: 1200px;
    overflow: hidden;
    background: var(--backdrop);
  }
  .flyer {
    position: absolute;
    left: 124px;
    top: 126px;
    width: 643px;
    height: 947px;
    background: var(--paper);
  }
  .brand {
    position: absolute;
    left: 129px;
    top: 40px;
    width: 385px;
    height: 583px;
    display: flex;
    flex-direction: column;
    align-items: center;
    justify-content: flex-end;
    padding-bottom: 30px;
  }
  .brand-square {
    width: 96px;
    height: 96px;
    background: var(--brand-blue);
    border-radius: 6px;
    margin-bottom: 40px;
  }
  .brand-name {
    font-family: "Bebas Neue", sans-serif;
    font-weight: 400;
    color: var(--brand-blue);
    text-align: center;
    line-height: 0.9;
  }
  .brand-name span { display: block; }
  .brand-name .line-keep { font-size: 170px; }
  .brand-name .line-harbor { font-size: 150px; }
  .brand-name .line-homestead { font-size: 84px; margin-top: 6px; }
  .pitch {
    position: absolute;
    left: 129px;
    top: 644px;
    width: 385px;
    font-family: "Arimo", Arial, sans-serif;
    font-size: 19.5px;
    line-height: 41.8px;
    color: var(--body-grey);
    text-transform: uppercase;
    text-align: justify;
    text-align-last: center;
  }
  .contact {
    position: absolute;
    left: 129px;
    top: 852px;
    width: 385px;
    height: 95px;
    background: var(--brand-blue);
    color: var(--on-blue);
    font-family: "Arimo", Arial, sans-serif;
    text-align: center;
    padding-top: 12px;
  }
  .contact-phone {
    display: block;
    font-weight: 700;
    font-size: 42px;
    line-height: 46px;
  }
  .contact-email {
    display: block;
    font-size: 19.5px;
    line-height: 24px;
  }
</style>
</head>
<body>
  <main class="flyer">
    <header class="brand">
      <div class="brand-square"></div>
      <h1 class="brand-name">
        <span class="line-keep">Keep</span>
        <span class="line-harbor">Harbor</span>
        <span class="line-homestead">Homestead</span>
      </h1>
    </header>
    <p class="pitch">Avoid short sale, foreclosure, repossession, negative credit inquires and all other negative actions associated with your real estate.</p>
    <footer class="contact">
      <span class="contact-phone">833-47-RENEW</span>
      <span class="contact-email">info@keepharborhomestead.com</span>
    </footer>
  </main>
</body>
</html>
```